Business Card Design

We are a commercial real estate brokerage in San Francisco, leasing office buildings downtown.
I would like a clean, elegant look. Simple but powerful .

Industry/Entity Type

Business

Contact Information for Business Card

Colin Farrow
lic# 07281549
415.555.0172
colin@tarvo-commercial.example
tarvo-commercial.example

```html
<!DOCTYPE html>
<html lang="en">
<head>
<meta charset="utf-8">
<title>Tarvo Commercial – Business Card</title>
<link rel="stylesheet" href="https://fonts.googleapis.com/css2?family=Open+Sans:wght@400;600;700&display=swap">
<style>
  :root {
    --page: #e9e9e7;
    --card: #f1f1f0;
    --brand-blue: #5f7596;
    --band-blue: #7188ab;
    --band-grey: #5a5e62;
    --ink: #2b2b2b;
    --ink-soft: #4a4a4a;
    --rule: #cfcfcf;
    --icon: #5a6f8c;
    --lic: #d4d6d8;
  }
  * { box-sizing: border-box; margin: 0; padding: 0; }
  html, body { width: 1200px; height: 768px; overflow: hidden; }
  body {
    background: var(--page);
    font-family: "Open Sans", sans-serif;
    position: relative;
  }
  .card {
    position: absolute;
    top: 229px;
    width: 540px;
    height: 310px;
    background: var(--card);
    box-shadow: 0 2px 6px rgba(0,0,0,0.12);
    overflow: hidden;
  }
  .card--front { left: 45px; }
  .card--back { left: 615px; }

  .wordmark {
    color: var(--brand-blue);
    font-weight: 700;
    text-transform: uppercase;
    line-height: 1;
    display: flex;
    align-items: center;
  }
  .wordmark__square {
    width: 18px; height: 18px;
    background: var(--brand-blue);
    margin-right: 14px;
    flex: none;
  }
  .wordmark__lines { display: flex; flex-direction: column; }
  .card--front .wordmark {
    position: absolute; left: 0; right: 0; top: 0; bottom: 0;
    justify-content: center;
  }
  .card--front .wordmark__primary { font-size: 56px; letter-spacing: 2px; }
  .card--front .wordmark__secondary { font-size: 24px; letter-spacing: 3px; margin-top: 4px; }

  .card--back .wordmark {
    position: absolute; left: 40px; top: 96px; width: 200px;
  }
  .card--back .wordmark__primary { font-size: 40px; letter-spacing: 1px; }
  .card--back .wordmark__secondary { font-size: 17px; letter-spacing: 2px; margin-top: 4px; }
  .card--back .wordmark__square { width: 14px; height: 14px; margin-right: 10px; }

  .divider {
    position: absolute; left: 262px; top: 70px;
    width: 1px; height: 120px; background: var(--rule);
  }
  .contact { position: absolute; left: 288px; top: 82px; }
  .contact__name { font-size: 20px; font-weight: 700; color: var(--ink); letter-spacing: 0.5px; }
  .contact__title { font-size: 11px; color: var(--ink-soft); margin-top: 1px; }
  .contact__list { list-style: none; margin-top: 18px; }
  .contact__item {
    display: flex; align-items: center;
    font-size: 13px; color: var(--ink); line-height: 22px;
  }
  .contact__item svg { width: 12px; height: 12px; margin-right: 10px; flex: none; }

  .bands { position: absolute; left: 0; bottom: 0; width: 540px; height: 110px; }
  .licence {
    position: absolute; left: 300px; bottom: 22px;
    font-size: 13px; color: var(--lic); letter-spacing: 0.5px;
  }
</style>
</head>
<body>
  <section class="card card--front" aria-label="Card front">
    <div class="wordmark">
      <span class="wordmark__square"></span>
      <span class="wordmark__lines">
        <span class="wordmark__primary">Tarvo</span>
        <span class="wordmark__secondary">Commercial</span>
      </span>
    </div>
  </section>

  <section class="card card--back" aria-label="Card back">
    <div class="wordmark">
      <span class="wordmark__square"></span>
      <span class="wordmark__lines">
        <span class="wordmark__primary">Tarvo</span>
        <span class="wordmark__secondary">Commercial</span>
      </span>
    </div>

    <div class="divider"></div>

    <div class="contact">
      <p class="contact__name">Colin Farrow</p>
      <p class="contact__title">Managing Director</p>
      <ul class="contact__list">
        <li class="contact__item">
          <svg viewBox="0 0 12 12" aria-hidden="true"><path fill="var(--icon)" d="M2.5 1h2l1 2.5-1.3 1a6 6 0 0 0 3.3 3.3l1-1.3L11 7.5v2A1.5 1.5 0 0 1 9.5 11 8.5 8.5 0 0 1 1 2.5 1.5 1.5 0 0 1 2.5 1z"/></svg>
          415.555.0172
        </li>
        <li class="contact__item">
          <svg viewBox="0 0 12 12" aria-hidden="true"><rect x="0.5" y="2" width="11" height="8" fill="var(--icon)"/><path d="M0.5 2l5.5 4.5L11.5 2" fill="none" stroke="var(--card)" stroke-width="1"/></svg>
          colin@tarvo-commercial.example
        </li>
        <li class="contact__item">
          <svg viewBox="0 0 12 12" aria-hidden="true"><circle cx="6" cy="6" r="5.5" fill="var(--icon)"/><path d="M0.5 6h11M6 0.5c-3 3-3 8 0 11M6 0.5c3 3 3 8 0 11" fill="none" stroke="var(--card)" stroke-width="0.8"/></svg>
          www.tarvo-commercial.example
        </li>
      </ul>
    </div>

    <svg class="bands" viewBox="0 0 540 110" aria-hidden="true">
      <polygon points="0,84 250,84 250,110 0,110" fill="var(--band-blue)"/>
      <polygon points="230,110 270,62 540,62 540,110" fill="var(--band-grey)"/>
    </svg>
    <p class="licence">LIC# 07281549</p>
  </section>
</body>
</html>
```